I have a business that exists already (Wrenfield Academy of Music) that we offer music lessons to all instruments. I recently opened a smaller version called CHORDS by Wrenfield that will only teach piano lessons. What I'm looking for now is a 3 page Website on word press. After I choose the design I like I want to be able to take over the website and bring it to our hosting company. We want full control of it and our team will take over. The reason I'm doing this is to have other visions and ideas from others. The first page will be about the company and our message/vision. Second page about the piano lessons. The third will be about franchising this concept "Chords by Wrenfield" Attached are 3 Logos . Please refer to our existing website www.wrenfieldmusicacademy.example to look at our piano page and franchising page. Please feel free to message me if you need more info. Thanks
Please note I do not want the new website (Chords by Wrenfield) To look like the other Website (Wrenfield Academy of Music) Fresh new look. I do not want the colours red or using the Red logo. I only provided it so that you have an Idea of What the other business looks like and that you can take the piano content and franchise content off of it. Chords by Wrenfield is smaller concept and only piano lessons.
Thanks
Target Market(s)
Only Piano lessons for all students
Number of Pages Required
3 page
Look and feel

```html
<!DOCTYPE html>
<html lang="en">
<head>
<meta charset="utf-8">
<title>Chords by Wrenfield – Piano Lessons</title>
<link href="https://fonts.googleapis.com/css2?family=Cinzel:wght@400;600&family=Mulish:wght@400;700&family=Lora:ital@1&family=Libre+Baskerville:wght@400;700&display=swap" rel="stylesheet">
<style>
:root{
  --blue:#2ea3f2;
  --ink:#222;
  --text:#555;
  --dark:#2b2b2b;
  --soft:#f6f2f6;
  --white:#fff;
  --black:#000;
  --quote:#999;
}
*{box-sizing:border-box;margin:0;padding:0}
html,body{width:1200px;height:3720px;overflow:hidden}
body{position:relative;background:var(--white);font-family:"Mulish",sans-serif;color:var(--text)}
.abs{position:absolute}
.btn{position:absolute;background:var(--blue);color:var(--white);font-family:"Cinzel",serif;font-size:17px;display:flex;align-items:center;justify-content:center;letter-spacing:.5px;box-shadow:0 2px 6px rgba(0,0,0,.15)}
.photo{position:absolute}

/* header */
.site-header{position:absolute;left:0;top:0;width:1200px;height:92px;background:var(--white)}
.brand{position:absolute;left:148px;top:26px;font-family:"Cinzel",serif;font-size:30px;color:var(--ink);display:flex;align-items:center;gap:10px}
.brand-dot{width:14px;height:14px;background:var(--ink)}
.nav{position:absolute;top:38px;font-family:"Cinzel",serif;font-size:14px;color:var(--ink);letter-spacing:1px}
.nav.active{color:var(--blue)}

/* hero */
.hero{position:absolute;left:0;top:92px;width:1200px;height:481px;background:linear-gradient(90deg,#c9c2bb 0%,#e9e5e2 35%,#f4f2f0 60%,#ece8e4 100%)}
.hero-copy{position:absolute;right:144px;text-align:right;font-family:"Cinzel",serif;color:var(--ink);white-space:nowrap}

/* about */
.section-title{position:absolute;font-family:"Cinzel",serif;font-size:34px;color:var(--ink)}
.section-title .accent{color:var(--blue)}
.title-rule{position:absolute;height:2px}
.lead{position:absolute;font-size:14px;line-height:25px;text-align:center;color:#444}
.feature-title{position:absolute;left:592px;top:812px;font-family:"Lora",serif;font-style:italic;font-size:31px;color:var(--blue)}
.feature-body{position:absolute;left:592px;top:864px;width:470px;font-size:14.5px;line-height:26px;color:#444}
.feature-body p+p{margin-top:4px}

/* vision */
.vision{position:absolute;left:0;top:1148px;width:1200px;height:340px;background:linear-gradient(180deg,#3a3a3a,#1e1e1e)}
.vision h2{position:absolute;top:62px;left:0;width:1200px;text-align:center;font-family:"Cinzel",serif;font-weight:400;font-size:32px;color:var(--white);letter-spacing:1px}
.vision p{position:absolute;top:128px;left:220px;width:760px;text-align:center;font-size:14.5px;line-height:25px;color:#ddd}

/* programs */
.programs-head{position:absolute;left:141px;top:1558px;border-left:7px solid var(--ink);padding-left:13px;font-family:"Libre Baskerville",serif;font-size:19px;line-height:25px;color:var(--blue);text-transform:uppercase}
.program-frame{position:absolute;left:141px;top:1632px;width:346px;height:313px;border:6px solid var(--blue)}
.program-card{position:absolute;width:268px;height:90px;background:var(--white);box-shadow:0 1px 6px rgba(0,0,0,.12)}
.program-card p{position:absolute;left:12px;top:14px;width:240px;border-left:3px solid var(--blue);padding-left:10px;font-size:12.5px;line-height:19px;color:#333}

/* franchise */
.franchise{position:absolute;left:0;top:2058px;width:1200px;height:247px;background:var(--soft)}
.franchise h2{position:absolute;top:54px;left:0;width:1200px;text-align:center;font-family:"Cinzel",serif;font-weight:400;font-size:38px;color:var(--ink);letter-spacing:1px}
.franchise p{position:absolute;top:115px;left:0;width:1200px;text-align:center;font-family:"Libre Baskerville",serif;font-size:16px;color:#333}

/* testimonial */
.quote-open{position:absolute;left:482px;top:2470px;font-family:"Libre Baskerville",serif;font-size:80px;color:var(--quote);line-height:1}
.quote-text{position:absolute;left:549px;top:2490px;white-space:nowrap;font-family:"Lora",serif;font-style:italic;font-size:22px;line-height:34px;color:#333}
.quote-close{display:inline-block;margin-left:20px;font-family:"Libre Baskerville",serif;font-style:normal;font-size:70px;line-height:0;vertical-align:-0.38em;color:var(--quote)}
.quote-author{position:absolute;left:549px;top:2576px;font-family:"Libre Baskerville",serif;font-weight:700;font-size:14.5px;color:#333}

/* contact */
.contact{position:absolute;left:0;top:2708px;width:1200px;height:667px;background:var(--soft)}
.contact-form{position:absolute;left:277px;top:2924px;width:358px;height:376px;background:var(--white);box-shadow:0 8px 20px rgba(0,0,0,.08)}
.field{position:absolute;left:28px;width:296px;height:35px;background:var(--white);box-shadow:0 1px 6px rgba(0,0,0,.14);font-family:"Mulish",sans-serif;font-style:italic;font-size:13px;color:#999;padding:0 14px;display:flex;align-items:center}
.field.area{height:94px;align-items:flex-start;padding-top:14px}
.send{position:absolute;left:32px;top:290px;width:296px;height:47px;background:var(--blue);color:var(--white);font-family:"Mulish",sans-serif;font-weight:700;font-size:18px;display:flex;align-items:center;justify-content:center}

/* footer */
.footer{position:absolute;left:0;top:3375px;width:1200px;height:310px;background:var(--black)}
.info{position:absolute;top:95px;width:300px;text-align:center;color:var(--white);font-size:14px;line-height:21px}
.info .icon{width:70px;height:70px;border-radius:50%;background:var(--white);margin:0 auto 18px;display:flex;align-items:center;justify-content:center}
.info h4{font-family:"Cinzel",serif;font-weight:400;font-size:14px;letter-spacing:1px}
.bottom-bar{position:absolute;left:0;top:3685px;width:1200px;height:35px;background:var(--blue);color:var(--white);font-size:12px}
.bottom-bar .copy{position:absolute;left:141px;top:10px}
.social{position:absolute;top:13px;width:10px;height:10px;border-radius:50%;background:var(--white)}
</style>
</head>
<body>

<header class="site-header">
  <div class="brand"><span class="brand-dot"></span>CHORDS by Wrenfield</div>
  <span class="nav active" style="left:596px">Home</span>
  <span class="nav" style="left:674px">Piano Lessons</span>
  <span class="nav" style="left:825px">Franchising</span>
  <span class="nav" style="left:963px">Contact Us</span>
</header>

<section class="hero" role="img" aria-label="Teacher and young student playing a white grand piano together in a bright room">
  <div class="hero-copy" style="top:135px;font-size:30px">We Provide</div>
  <div class="hero-copy" style="top:176px;font-size:46px;font-weight:600">Piano Lessons</div>
  <div class="hero-copy" style="top:236px;font-size:30px">For All Students</div>
  <div class="btn" style="left:875px;top:292px;width:183px;height:35px">Contact Us Today</div>
</section>

<section class="about">
  <h2 class="section-title" style="left:0;width:1200px;text-align:center;top:633px"><span class="accent">About</span> CHORDS by Wrenfield</h2>
  <div class="title-rule" style="left:510px;top:680px;width:115px;background:var(--blue)"></div>
  <div class="title-rule" style="left:625px;top:680px;width:115px;background:var(--ink)"></div>
  <p class="lead" style="left:170px;top:690px;width:860px">Lorem hendrerit in vulputate velit esse molestie consequat, velocity illum dolore eu feugiat nulla facilisis at vero eros et accumsan etlict iusto odio dignissim qui blandit praesent luptatum zzril delenit loei augue duis dolore te feugait nulla facilisi.</p>

  <div class="abs" style="left:240px;top:786px;width:230px;height:265px;border:14px solid #e4e4e4"></div>
  <div class="photo" role="img" aria-label="Young students practising piano in a group class" style="left:141px;top:762px;width:275px;height:245px;background:linear-gradient(135deg,#5d5a5c,#8f7f73 55%,#c7b6a6)"></div>
  <div class="photo" role="img" aria-label="Black grand piano on a stage in a classroom" style="left:293px;top:833px;width:274px;height:244px;background:linear-gradient(180deg,#d9d2c8 0%,#b6ada2 55%,#8a6b45 100%);box-shadow:4px 4px 0 #e4e4e4"></div>

  <h3 class="feature-title">Playing the Piano</h3>
  <div class="feature-body">
    <p>When you think of a piano, you probably envision black and white keys but the piano is more than those harmonious sounds created by the player. The versatility and the musicianship instilled into the player from those keys is the true magic that comes from playing piano!</p>
    <p>Starting from the grassroots, experience different methods and styles of playing piano.</p>
  </div>
  <div class="btn" style="left:592px;top:1033px;width:155px;height:35px">Read More</div>
</section>

<section class="vision" role="img" aria-label="Close-up of piano keys in dark light">
  <h2>Our Vision</h2>
  <div class="title-rule" style="left:540px;top:110px;width:120px;background:var(--blue)"></div>
  <p>Our Mission is Lorem ipsum dolor sit amet, consectetuer adipiscig elit, sed diama nonummy nibh euismod tincidunt ut laoreet dolore magna aliquam erat volutpat. Ut wisi enim ad minim veniam. Lorem hendrerit in vulputate velit esse molestie consequat, velocity illum dolore eu feugiat nulla facilisis at vero eros.</p>
  <div class="btn" style="left:510px;top:224px;width:182px;height:36px">Contact Us Today</div>
</section>

<section class="programs">
  <h3 class="programs-head">Our programs also provide<br>students the opportunity to:</h3>
  <div class="program-frame"><div role="img" aria-label="Students playing digital pianos in a practice room" style="width:100%;height:100%;background:linear-gradient(135deg,#f2f2f2,#d8d4d0 50%,#5c4a3e)"></div></div>
  <div class="program-card" style="left:514px;top:1635px"><p>Participate in large-scale performances.</p></div>
  <div class="program-card" style="left:791px;top:1635px"><p>Perform at Wrenfield's many community events on a regular basis.</p></div>
  <div class="program-card" style="left:514px;top:1740px"><p>Access the GTA's coolest Broadcast stage</p></div>
  <div class="program-card" style="left:791px;top:1740px"><p>Attend Clinics, Masterclasses, and Jam Nights</p></div>
  <div class="program-card" style="left:514px;top:1845px"><p>Access the Wrenfield Rocks band program. Wrenfield's Band Program empowers.</p></div>
  <div class="program-card" style="left:791px;top:1845px"><p>Register in our elite teaching program to learn how to pass on the magic.</p></div>
</section>

<section class="franchise">
  <h2>Franchise Opportunities</h2>
  <p>BE PART OF THE WRENFIELD ACADEMY FAMILY</p>
  <div class="btn" style="left:530px;top:150px;width:140px;height:35px">Know More</div>
</section>

<section class="testimonial">
  <svg class="abs" style="left:190px;top:2380px" width="260" height="260" viewBox="0 0 260 260">
    <circle cx="78" cy="80" r="78" fill="var(--blue)"/>
    <circle cx="142" cy="144" r="113" fill="var(--white)"/>
  </svg>
  <div class="photo" role="img" aria-label="Portrait of the quoted pianist" style="left:222px;top:2417px;width:220px;height:220px;border-radius:50%;background:radial-gradient(circle at 45% 40%,#c9a58c,#8a6f60 60%,#e6e6e6 100%)"></div>
  <span class="quote-open">&ldquo;</span>
  <p class="quote-text">Life is like a piano. What you get out of it depends<br>on how you play it.<span class="quote-close">&rdquo;</span></p>
  <p class="quote-author">- THEO MARLOWE</p>
</section>

<section class="contact">
  <h2 class="section-title" style="left:0;width:1200px;text-align:center;top:60px"><span class="accent">Contact</span> Us</h2>
  <div class="title-rule" style="left:494px;top:110px;width:106px;background:var(--blue)"></div>
  <div class="title-rule" style="left:600px;top:110px;width:65px;background:var(--ink)"></div>
  <p class="lead" style="left:210px;top:132px;width:780px">Lorem Ipsum is Lorem ipsum dolor sit amet, consectetuer adipiscig elit, sed diama nonummy nibh euismod tincidunt ut laoreet dolore magna aliquam erat volutpat. Ut wisi enim ad minim veniam.</p>
</section>
<form class="contact-form">
  <div class="field" style="top:29px">First Name</div>
  <div class="field" style="top:80px">Last Name</div>
  <div class="field" style="top:130px">What's Your Email?</div>
  <div class="field area" style="left:32px;top:181px">Your Questions...</div>
  <div class="send">SEND MESSGAE</div>
</form>
<div class="photo" role="img" aria-label="Street map showing the academy location" style="left:635px;top:2910px;width:311px;height:394px;background:linear-gradient(135deg,#eceae4,#dfe8d2 50%,#f1ead6)"></div>

<footer class="footer">
  <div class="info" style="left:163px">
    <div class="icon"><svg width="30" height="34" viewBox="0 0 24 28"><path d="M12 1a9 9 0 0 0-9 9c0 7 9 17 9 17s9-10 9-17a9 9 0 0 0-9-9z" fill="var(--blue)"/><circle cx="12" cy="10" r="3.5" fill="var(--white)"/></svg></div>
    <h4>Chords by Wrenfield</h4>
    <p>123, Building Name, Street<br>City, State XY 123456</p>
  </div>
  <div class="info" style="left:456px">
    <div class="icon"><svg width="30" height="30" viewBox="0 0 24 24"><path d="M6.6 10.8a15 15 0 0 0 6.6 6.6l2.2-2.2a1 1 0 0 1 1-.25 11.4 11.4 0 0 0 3.6.57 1 1 0 0 1 1 1V20a1 1 0 0 1-1 1A17 17 0 0 1 3 4a1 1 0 0 1 1-1h3.5a1 1 0 0 1 1 1c0 1.25.2 2.45.57 3.57a1 1 0 0 1-.25 1z" fill="var(--blue)"/></svg></div>
    <h4>Call Us</h4>
    <p>1-888-555-0142</p>
  </div>
  <div class="info" style="left:739px">
    <div class="icon"><svg width="32" height="24" viewBox="0 0 32 24"><rect x="1" y="2" width="30" height="20" rx="2" fill="var(--blue)"/><path d="M2 4l14 10L30 4" stroke="var(--white)" stroke-width="2" fill="none"/></svg></div>
    <h4>Email Us</h4>
    <p>inquiry@chordsbywrenfield.example</p>
  </div>
</footer>
<div class="bottom-bar">
  <span class="copy">Copyright © 2020 <b>Chords by Wrenfield</b>. All Rights Reserved.</span>
  <span class="social" style="left:964px" aria-label="Social link"></span>
  <span class="social" style="left:988px" aria-label="Social link"></span>
  <span class="social" style="left:1015px" aria-label="Social link"></span>
  <span class="social" style="left:1043px" aria-label="Social link"></span>
</div>

</body>
</html>
```